Packaging box design for start up candle company based in Sydney Australia

I need an eye catching box design for my candle company called Midnight Wickhouse. We specialise only in delicious cake and cocktail scented candles. I want to convey a sense of elegant whimsy.
I have a logo and a style guide which I'm happy with, but need to complete the brand with a stunning box design.
I'd like the same design for two different sized boxes.

```html
<!DOCTYPE html>
<html lang="en">
<head>
<meta charset="utf-8">
<title>Midnight Wickhouse — Candle Box Dieline</title>
<link rel="stylesheet" href="https://fonts.googleapis.com/css2?family=Cormorant+Garamond:wght@600&family=Courier+Prime&family=Allura&display=swap">
<style>
  :root {
    --stage: #e7ebea;
    --board: #ffffff;
    --cut-line: #3bb3e6;
    --fold-line: #ececec;
    --ink: #1f1d1f;
    --coral: #e7877a;
    --peach: #fcd3b6;
    --sage: #cfe6c4;
    --blush: #f3d0dd;
    --mint: #b9e2d7;
    --butter: #fdf6d8;
  }
  html, body {
    margin: 0;
    padding: 0;
    width: 1200px;
    height: 1200px;
    overflow: hidden;
    background: var(--stage);
  }
  .canvas {
    position: relative;
    width: 1200px;
    height: 1200px;
  }
  .dieline {
    position: absolute;
    left: 50px;
    top: 178px;
    width: 1100px;
    height: 845px;
  }
  .cut { fill: var(--board); stroke: var(--cut-line); stroke-width: 2; }
  .fold { stroke: var(--fold-line); stroke-width: 1.5; fill: none; }
  .brand-name {
    font-family: "Cormorant Garamond", "Times New Roman", serif;
    font-weight: 600;
    font-size: 34px;
    letter-spacing: 5px;
    fill: var(--ink);
    text-anchor: middle;
  }
  .brand-rule { stroke: var(--coral); stroke-width: 1.5; }
  .tagline {
    font-family: "Allura", cursive;
    font-size: 30px;
    fill: var(--coral);
    text-anchor: middle;
  }
  .product-note {
    font-family: "Courier Prime", "Courier New", monospace;
    font-size: 15px;
    fill: var(--coral);
    text-anchor: middle;
  }
  .pattern { opacity: 0.55; }
</style>
</head>
<body>
<main class="canvas">
  <svg class="dieline" viewBox="40 10 1490 1145" xmlns="http://www.w3.org/2000/svg">
    <defs>
      <linearGradient id="wash-peach" x1="0" y1="0" x2="1" y2="1">
        <stop offset="0" stop-color="var(--butter)"/>
        <stop offset="0.5" stop-color="var(--peach)"/>
        <stop offset="1" stop-color="var(--blush)"/>
      </linearGradient>
      <linearGradient id="wash-sage" x1="0" y1="0" x2="1" y2="1">
        <stop offset="0" stop-color="var(--sage)"/>
        <stop offset="0.6" stop-color="var(--butter)"/>
        <stop offset="1" stop-color="var(--peach)"/>
      </linearGradient>
      <linearGradient id="wash-blush" x1="1" y1="0" x2="0" y2="1">
        <stop offset="0" stop-color="var(--sage)"/>
        <stop offset="0.5" stop-color="var(--blush)"/>
        <stop offset="1" stop-color="var(--mint)"/>
      </linearGradient>
      <linearGradient id="wash-mint" x1="1" y1="0" x2="0" y2="1">
        <stop offset="0" stop-color="var(--blush)"/>
        <stop offset="0.5" stop-color="var(--butter)"/>
        <stop offset="1" stop-color="var(--mint)"/>
      </linearGradient>
    </defs>

    <!-- die cut outline -->
    <path class="cut" d="M805 270 L805 60 Q805 15 850 15 L1135 15 Q1180 15 1180 60 L1180 270 L1460 270 Q1490 270 1495 300 L1510 410 L1525 425 L1525 885 L1340 1065 L1215 1065 L1190 925 L1168 903 L1176 915 L1176 1152 L1060 1152 L1022 1065 L1007 1065 L1007 1080 L970 1152 L815 1152 L805 915 L650 1065 L525 1065 L497 925 L475 903 L485 915 L485 1152 L368 1152 L330 1065 L315 1065 L315 1080 L278 1152 L122 1152 L113 890 L43 875 L43 448 L125 430 L460 430 L475 415 L490 295 Q495 270 525 270 Z"/>

    <!-- pastel pattern washes -->
    <rect class="pattern" role="img" aria-label="Soft pastel abstract shapes in peach, butter and blush" x="128" y="445" width="345" height="435" fill="url(#wash-peach)"/>
    <rect class="pattern" role="img" aria-label="Soft pastel abstract shapes in sage, butter and peach" x="473" y="445" width="345" height="435" fill="url(#wash-sage)"/>
    <rect class="pattern" role="img" aria-label="Soft pastel abstract shapes in sage, blush and mint" x="818" y="445" width="347" height="435" fill="url(#wash-blush)"/>
    <rect class="pattern" role="img" aria-label="Soft pastel abstract shapes in blush, butter and mint" x="1165" y="445" width="345" height="435" fill="url(#wash-mint)"/>
    <rect class="pattern" role="img" aria-label="Soft pastel abstract shapes in peach, sage and butter" x="818" y="100" width="347" height="345" fill="url(#wash-sage)"/>

    <!-- fold lines -->
    <g class="fold">
      <line x1="128" y1="445" x2="1510" y2="445"/>
      <line x1="128" y1="880" x2="1510" y2="880"/>
      <line x1="818" y1="100" x2="1165" y2="100"/>
      <line x1="128" y1="445" x2="128" y2="880"/>
      <line x1="473" y1="445" x2="473" y2="880"/>
      <line x1="818" y1="100" x2="818" y2="880"/>
      <line x1="1165" y1="100" x2="1165" y2="880"/>
    </g>

    <!-- lid panel, upside down -->
    <g class="panel-lid" transform="rotate(180 992 290)">
      <line class="brand-rule" x1="872" y1="250" x2="1112" y2="250"/>
      <text class="brand-name" x="992" y="285" style="font-size:26px">MIDNIGHT</text>
      <text class="brand-name" x="992" y="313" style="font-size:26px">WICKHOUSE</text>
    </g>

    <!-- side panel one -->
    <g class="panel-side">
      <line class="brand-rule" x1="180" y1="525" x2="422" y2="525"/>
      <text class="brand-name" x="300" y="563">MIDNIGHT</text>
      <text class="brand-name" x="300" y="597">WICKHOUSE</text>
      <text class="tagline" x="300" y="818">Comfort food in candle form</text>
    </g>

    <!-- front panel -->
    <g class="panel-front">
      <line class="brand-rule" x1="526" y1="525" x2="768" y2="525"/>
      <text class="brand-name" x="647" y="563">MIDNIGHT</text>
      <text class="brand-name" x="647" y="597">WICKHOUSE</text>
      <text class="product-note" x="647" y="811">Natural coconut soy candle</text>
      <text class="product-note" x="647" y="830">Hand poured in Sydney's inner west</text>
    </g>

    <!-- side panel two -->
    <g class="panel-side">
      <line class="brand-rule" x1="871" y1="525" x2="1113" y2="525"/>
      <text class="brand-name" x="992" y="563">MIDNIGHT</text>
      <text class="brand-name" x="992" y="597">WICKHOUSE</text>
      <text class="tagline" x="992" y="818">Comfort food in candle form</text>
    </g>

    <!-- back panel -->
    <g class="panel-back">
      <line class="brand-rule" x1="1217" y1="525" x2="1459" y2="525"/>
      <text class="brand-name" x="1338" y="563">MIDNIGHT</text>
      <text class="brand-name" x="1338" y="597">WICKHOUSE</text>
      <text class="product-note" x="1338" y="811">Natural coconut soy candle</text>
      <text class="product-note" x="1338" y="830">Hand poured in Sydney's inner west</text>
    </g>
  </svg>
</main>
</body>
</html>
```